BrookvaleLogic Website Design

To design a website for BrookvaleLogic, a software development company. The website should reflect the branding of our company, which is Smart, Beautiful, and Sophisticated. The existing website is www.brookvalelogic-example.com.sg

```html
<!DOCTYPE html>
<html lang="en">
<head>
<meta charset="utf-8">
<title>BrookvaleLogic – A software development company</title>
<link href="https://fonts.googleapis.com/css2?family=Arimo:wght@400;700&family=Squada+One&display=swap" rel="stylesheet">
<style>
:root{
  --navy:#0f4566;
  --navy-deep:#0b3552;
  --blue:#1a7ab8;
  --band:#e9e9e9;
  --soft:#f2f2f2;
  --line:#dcdcdc;
  --text:#777;
  --nav-text:#333;
  --white:#fff;
  --hero-a:#c9c1b3;
  --hero-b:#dccdb4;
}
*{margin:0;padding:0;box-sizing:border-box}
html,body{width:1200px;height:938px;overflow:hidden;background:var(--white);font-family:"Arimo",Arial,sans-serif}
.page{position:relative;width:1200px;height:938px}
.topline{position:absolute;left:271px;top:0;width:659px;height:6px;background:var(--navy)}
.header-band{position:absolute;left:271px;top:6px;width:659px;height:149px;background:var(--band)}
.brand{position:absolute;left:0;width:1200px;top:34px;display:flex;justify-content:center;align-items:center;gap:10px}
.brand-mark{width:46px;height:46px;border-radius:50%;background:var(--navy)}
.brand-text{display:flex;flex-direction:column;align-items:flex-end}
.brand-name{font-size:24px;font-weight:400;color:var(--navy);letter-spacing:.3px}
.brand-tag{font-size:7px;color:var(--navy-deep);margin-top:1px}
.nav{position:absolute;left:343px;top:114px;width:515px;height:29px;background:linear-gradient(#f6f6f6,#e2e2e2);border:1px solid #c9c9c9;display:flex;padding-left:38px;box-shadow:0 1px 2px rgba(0,0,0,.15)}
.nav a{display:flex;align-items:center;padding:0 14px;font-size:9px;color:var(--nav-text);text-decoration:none;border-right:1px solid #c9c9c9;letter-spacing:.2px}
.nav a.active{background:var(--navy);color:var(--white);padding:0 10px}
.nav a:first-child{border-left:1px solid #c9c9c9}
.slider{position:absolute;left:343px;top:143px;width:515px;height:126px;overflow:hidden}
.slide-visual{position:absolute;inset:0;background:linear-gradient(90deg,var(--hero-a),var(--hero-b))}
.slide-copy{position:absolute;right:28px;top:62px;text-align:right;font-size:13px;line-height:16px;font-weight:700;color:#4a4a4a}
.slider .arrow{position:absolute;top:50px}
.slider .arrow.prev{left:22px}
.slider .arrow.next{right:6px}
.dots{position:absolute;left:242px;top:113px;display:flex;gap:11px}
.dots span{width:7px;height:7px;border-radius:50%;background:#8a8580}
.dots span.on{background:#111}
.section-title{position:absolute;left:0;width:1200px;text-align:center;font-family:"Squada One",sans-serif;font-weight:400;color:var(--navy)}
.t-products{top:292px;font-size:21px;color:var(--blue)}
.services{position:absolute;left:344px;top:329px;width:514px;height:129px;border:1px solid var(--line);display:flex}
.service{flex:1;border-right:1px solid var(--line);display:flex;flex-direction:column;align-items:center;padding-top:23px}
.service:last-child{border-right:none}
.service .icon{width:63px;height:63px;border-radius:50%;background:radial-gradient(circle at 50% 35%,#1d5a80,var(--navy-deep));display:flex;align-items:center;justify-content:center}
.service p{margin-top:13px;font-size:8px;color:var(--text)}
.mission{position:absolute;left:271px;top:476px;width:659px;height:118px;background:var(--soft)}
.t-mission{top:17px;left:0;width:659px;font-size:22px}
.mission p{position:absolute;left:108px;width:443px;top:50px;text-align:center;font-size:6.6px;line-height:13px;color:#888}
.t-team{top:622px;font-size:25px}
.team{position:absolute;top:667px;left:0;width:1200px;display:flex;justify-content:center;gap:17px}
.member{width:87px;display:flex;flex-direction:column;align-items:center}
.portrait{width:87px;height:87px;border-radius:50%;border:5px solid #ececec;background:radial-gradient(circle,#b9a294,#e6e2de)}
.member span{margin-top:10px;font-size:6px;color:#888}
.footer{position:absolute;left:271px;top:802px;width:659px;height:136px;background:var(--navy);color:var(--white)}
.footer-links{position:absolute;left:72px;top:29px;list-style:none}
.footer-links li{font-size:7.5px;height:15.5px}
.footer-address{position:absolute;left:180px;top:29px;font-size:7.5px;line-height:8.7px;font-style:normal}
.footer-address .company{margin-bottom:9px}
.copyright{position:absolute;right:72px;top:100px;font-size:6px}
</style>
</head>
<body>
<div class="page">
  <div class="topline"></div>
  <div class="header-band"></div>

  <div class="brand">
    <div class="brand-mark"></div>
    <div class="brand-text">
      <span class="brand-name">BrookvaleLogic</span>
      <span class="brand-tag">A software development company</span>
    </div>
  </div>

  <nav class="nav">
    <a class="active" href="#">HOME</a>
    <a href="#">COMPANY PROFILE</a>
    <a href="#">BOARD OF DIRECTORS</a>
    <a href="#">ABOUT US</a>
    <a href="#">CONTACT US</a>
  </nav>

  <div class="slider">
    <div class="slide-visual" role="img" aria-label="Banner photo of a tablet on a light wooden desk"></div>
    <svg class="arrow prev" width="12" height="22" viewBox="0 0 12 22"><path d="M10 2 2 11l8 9" fill="none" stroke="#555" stroke-width="3"/></svg>
    <svg class="arrow next" width="12" height="22" viewBox="0 0 12 22"><path d="M2 2l8 9-8 9" fill="none" stroke="#555" stroke-width="3"/></svg>
    <p class="slide-copy">We produce high interactive<br>digital media and software<br>for the mobile world</p>
    <div class="dots"><span class="on"></span><span></span><span></span></div>
  </div>

  <h2 class="section-title t-products">PRODUCTS AND SERVICES</h2>
  <div class="services">
    <div class="service">
      <div class="icon"><svg width="24" height="30" viewBox="0 0 24 30"><path d="M2 2h13l7 7v19H2z" fill="none" stroke="#fff" stroke-width="2.2" stroke-linejoin="round"/></svg></div>
      <p>Software Applications</p>
    </div>
    <div class="service">
      <div class="icon"><svg width="32" height="34" viewBox="0 0 32 34"><rect x="3" y="2" width="15" height="26" rx="2" fill="none" stroke="#fff" stroke-width="2"/><rect x="16" y="12" width="12" height="20" rx="2" fill="var(--navy-deep)" stroke="#fff" stroke-width="2"/><path d="M7 14l6-7M20 24l4-6" stroke="#fff" stroke-width="1.2"/></svg></div>
      <p>Mobile Applications</p>
    </div>
    <div class="service">
      <div class="icon"><svg width="40" height="28" viewBox="0 0 40 28"><path d="M9 26a7 7 0 0 1 0-14 10 10 0 0 1 19-3 8 8 0 0 1 3 17z" fill="#fff"/><path d="M20 23v-10M15 17l5-5 5 5" fill="none" stroke="var(--navy-deep)" stroke-width="3"/></svg></div>
      <p>Hosting</p>
    </div>
    <div class="service">
      <div class="icon"><svg width="34" height="32" viewBox="0 0 34 32"><g fill="none" stroke="#fff"><circle cx="12" cy="20" r="5" stroke-width="5" stroke-dasharray="3 2.2"/><circle cx="12" cy="20" r="3.5" stroke-width="2.5"/><circle cx="24" cy="9" r="4" stroke-width="4" stroke-dasharray="2.5 1.7"/><circle cx="24" cy="9" r="2.7" stroke-width="2"/></g></svg></div>
      <p>Maintenance Services</p>
    </div>
  </div>

  <section class="mission">
    <h2 class="section-title t-mission">MISSION AND VISION</h2>
    <p>BrookvaleLogic is fully committed to assist our customers and partners to engage and be part of the digital revolution. We vision computing will be invisible and mobile technologies and smart media will be the enabling agents. BrookvaleLogic intend to be a leading and well respected global software and technology company that is fully committed to delivering excellent service and products to our customers and partners.</p>
  </section>

  <h2 class="section-title t-team">THE TEAM</h2>
  <div class="team">
    <div class="member"><div class="portrait" role="img" aria-label="Portrait photo of a team member"></div><span>Name goes here..</span></div>
    <div class="member"><div class="portrait" role="img" aria-label="Portrait photo of a team member"></div><span>Name goes here..</span></div>
    <div class="member"><div class="portrait" role="img" aria-label="Portrait photo of a team member"></div><span>Name goes here..</span></div>
    <div class="member"><div class="portrait" role="img" aria-label="Portrait photo of a team member"></div><span>Name goes here..</span></div>
  </div>

  <footer class="footer">
    <ul class="footer-links">
      <li>Board Of Directors</li>
      <li>Products &amp; Services</li>
      <li>We are Hiring</li>
      <li>Contact Us</li>
      <li>Locate Us</li>
    </ul>
    <address class="footer-address">
      <div class="company">BrookvaleLogic Pte Ltd</div>
      No.8 Alder Lane, #03-17<br>
      Harbourview Centre<br>
      Singapore 048812<br>
      (DID): (65) 6100 2471<br>
      Tel: (65) 6100 2400<br>
      Fax: (65) 6100 2499<br>
      hello@brookvalelogic-example.com.sg
    </address>
    <div class="copyright">Copyright © 2014 BrookvaleLogic</div>
  </footer>
</div>
</body>
</html>
```